Design clean technology service-based company website

Hello, We are looking to reskin our company website. We are an environmental inspection company and test for Asbestos, Lead and Mold along with other contaminants. People depend on the results to be accurate and fast. We are regulated by the EPA and State regulations. We work a lot with business to business and business to customer. We are wanting to make our new presentation to be modern and easy for customers to interact with us, understand our process and services while providing valuable environmental informational resource and updates. We are a technology based company and will be providing instantaneous results as reports come in for the customers. We are needing good calls to action on the site to direct them to setup a new inspection. Each user will have a backend access to their job information with invoices, reports, status, etc. We have developed software to be able to proved these reports and want to look the part.

My current website is www.trypelmarix.com

Helllo we are wanting to make sure we have good time to select the right website for us and also have the additional time to select other pages of the website. We have received great designs and have consolidated our requests into a document for the next set of iterations.

Target Market(s)

Home Owners, Contractors, Engineers, Real Estate Agents, Building Owners, Insurance Adjusters

Industry/Entity Type

Environmental Consultant

Number of Pages Required

5+ page

Font styles to use
Sans Serif

Colors
0355a3
9bcb3c
7f7f7f
f5f5f5
000000

Requirements
Must have
• Use our existing logo to design around
• The layouts look good in mobile mode for understanding and selecting services and signing up
• Clean Modern Layout
• Have all pages on the website have a similar layout and feel
• Clearly communicate services along with bundle service packages
• Detail the customer journey with graphic design
• Great call to actions to either schedule inspection online, call, text, chat
Nice to have
• Have an interactive graphic for where to test for lead, asbestos and mold.
• I like the barney kolts top order line bar - see attached
• Have clear question and answer page layouts for asbestos, lead and mold
• Show Company reviews
• Have clear Resources pages for all types of contaminants
Should not have
• My current website is www.trypelmarix.com

```html
<!DOCTYPE html>
<html lang="en">
<head>
<meta charset="utf-8">
<title>Tervane – Environmental Inspections</title>
<link href="https://fonts.googleapis.com/css2?family=Exo+2:wght@400;500;600&family=Montserrat:wght@400;500;600&display=swap" rel="stylesheet">
<style>
:root{
  --blue:#1f6fbf;
  --blue-deep:#0355a3;
  --green:#8cc63f;
  --green-light:#9bcb3c;
  --grey:#7f7f7f;
  --light:#f5f5f5;
  --ink:#111111;
  --text:#6a6a6a;
  --white:#ffffff;
}
*{margin:0;padding:0;box-sizing:border-box}
html,body{width:1200px;height:3524px;overflow:hidden;background:var(--white)}
body{position:relative;font-family:"Montserrat",sans-serif;color:var(--text)}
.abs{position:absolute}
h1,h2,h3{font-weight:500}

/* header */
.site-header{left:0;top:0;width:1200px;height:128px;background:var(--white)}
.brand{left:111px;top:32px;display:flex;align-items:center;gap:12px}
.brand-dot{width:26px;height:26px;border-radius:50%;background:var(--green)}
.brand-name{font-family:"Exo 2",sans-serif;font-weight:600;font-size:44px;color:var(--green);letter-spacing:.5px}
.top-bar{left:402px;top:19px;width:685px;height:59px;background:var(--green);display:flex;align-items:center;padding:0 24px;color:var(--white);font-size:13px;gap:34px}
.top-bar .contact{display:flex;align-items:center;gap:8px}
.socials{margin-left:auto;display:flex;gap:10px}
.social{width:30px;height:30px;border-radius:50%}
.s1{background:#3b5998}.s2{background:#1da1f2}.s3{background:#d93a30}.s4{background:#0e76a8}
.main-nav{left:402px;top:90px;width:685px;display:flex;justify-content:space-between;font-size:13.5px;font-weight:500;color:#333;letter-spacing:.3px}
.main-nav .active{color:var(--ink);position:relative}
.main-nav .active::after{content:"";position:absolute;left:0;right:0;bottom:-10px;height:3px;background:var(--green)}

/* hero */
.hero{left:0;top:128px;width:1200px;height:557px;background:linear-gradient(180deg,#5b6b5a 0%,#4c5a44 45%,#3f5a2f 80%,#51733a 100%)}
.hero-frame{left:246px;top:338px;width:708px;height:141px;border:3px solid rgba(255,255,255,.8);border-top:none}
.frame-top{top:338px;height:3px;background:rgba(255,255,255,.8)}
.hero-title{left:0;top:298px;width:1200px;text-align:center;font-family:"Exo 2",sans-serif;font-weight:500;font-size:54px;line-height:62px;color:var(--white)}
.btn{display:flex;align-items:center;justify-content:center;border-radius:30px;font-size:15px;font-weight:600;color:var(--white);letter-spacing:.5px}
.hero-btn{left:489px;top:456px;width:222px;height:40px;background:var(--green)}

/* services */
.service-panel{left:111px;top:645px;width:489px;height:527px;background:var(--blue)}
.service-title{left:111px;top:676px;width:489px;text-align:center;font-family:"Exo 2",sans-serif;font-size:32px;color:var(--white)}
.service-text{left:121px;top:752px;width:469px;text-align:center;font-size:11.5px;line-height:22px;color:var(--white)}
.service-card{top:815px;width:302px;height:338px}
.card-a{left:135px;background:linear-gradient(180deg,#9fc3e3 0%,#b99a82 45%,#6c7a4e 100%)}
.card-b{left:456px;background:linear-gradient(180deg,#dfe6ec 0%,#c4c8c8 50%,#6b8a57 100%)}
.card-c{left:777px;background:linear-gradient(135deg,#2d3c55 0%,#c99d82 55%,#3a3f4e 100%)}
.service-label{top:1075px;height:61px;display:flex;align-items:center;justify-content:center;font-size:15px;font-weight:500}
.label-a{left:182px;width:208px;background:var(--green);color:var(--white)}
.label-b{left:501px;width:212px;background:var(--white);color:var(--ink)}
.label-c{left:820px;width:211px;background:var(--white);color:var(--ink)}

/* construction band */
.project-band{left:0;top:1224px;width:1200px;height:158px;background:linear-gradient(100deg,#8cc63f 0%,#9bcb3c 50%,#86c13a 100%)}
.project-title{left:111px;top:1256px;font-family:"Exo 2",sans-serif;font-size:29px;color:var(--white)}
.project-text{left:111px;top:1300px;width:720px;font-size:12.5px;line-height:24px;font-weight:600;color:var(--white)}
.project-btn{left:902px;top:1283px;width:196px;height:40px;background:var(--green);border:2px solid var(--white)}

/* environmental testing */
.section-heading{font-family:"Exo 2",sans-serif;font-weight:500;color:var(--ink)}
.env-heading{left:111px;top:1485px;font-size:32px;line-height:37px;letter-spacing:.5px}
.rule{height:3px;background:var(--green);width:78px}
.env-rule{left:111px;top:1575px}
.body-copy{font-size:12.5px;line-height:25px;color:var(--text)}
.env-copy{left:111px;top:1603px;width:460px}
.env-copy p+p{margin-top:14px}
.env-media-a{left:600px;top:1434px;width:249px;height:397px;background:linear-gradient(180deg,#b9d6e8 0%,#8fae6a 45%,#6e8d4b 100%)}
.env-media-b{left:849px;top:1434px;width:249px;height:397px;background:linear-gradient(180deg,#a7b5c1 0%,#7b6a5a 45%,#4f7a3c 100%)}
.play{width:34px;height:34px;border:2px solid var(--white);border-radius:50%;top:1614px}

/* about */
.about{left:0;top:1918px;width:1200px;height:378px;background:linear-gradient(180deg,#e4e4e4 0%,#cfcfcf 100%)}
.about-shape{left:0;top:1918px}
.about-pill{left:196px;top:1960px;width:123px;height:303px;border-radius:62px;background:var(--green)}
.about-photo{left:156px;top:2012px;width:205px;height:208px;border:5px solid var(--white);background:linear-gradient(180deg,#9ab88a 0%,#6a7c8c 60%,#55606e 100%);box-shadow:0 2px 6px rgba(0,0,0,.25)}
.about-heading{left:600px;top:1960px;font-size:32px}
.about-rule{left:600px;top:2015px;width:78px;height:3px;background:var(--ink)}
.about-copy{left:600px;top:2035px;width:460px}
.about-copy p+p{margin-top:12px}
.signature{left:945px;top:2234px;font-family:"Exo 2",sans-serif;font-weight:500;font-size:12px;color:#333;letter-spacing:1px}
.owner{left:945px;top:2260px;font-size:11px;color:var(--grey)}

/* partner badges */
.badges{left:0;top:2296px;width:1200px;height:151px;background:var(--blue)}
.badge{background:rgba(255,255,255,.9)}

/* testimonials */
.testi-heading{left:0;top:2488px;width:1200px;text-align:center;font-size:32px}
.testi-rule{left:561px;top:2546px;width:78px;height:2px;background:#333}
.quote{top:2589px;width:339px;height:104px;border:1px solid #cfcfcf;background:var(--white);padding:14px 18px;font-size:12px;line-height:19px;font-style:italic;color:#444;text-align:center}
.avatar{width:56px;height:56px;border-radius:50%;top:2672px;border:2px solid var(--white)}
.av1{left:280px;background:linear-gradient(180deg,#e9c89c,#d8a46c)}
.av2{left:645px;background:linear-gradient(180deg,#d9c4b0,#9a7a5c)}
.person{top:2737px;width:120px;text-align:center;font-size:12.5px;color:#333}
.stars{top:2758px;width:120px;text-align:center;font-size:11px;color:#f2b01e;letter-spacing:1px}

/* blog */
.blog-band{left:0;top:2825px;width:1200px;height:246px;background:linear-gradient(120deg,#1a64b2 0%,#2a7ccc 50%,#1c6abb 100%)}
.blog-base{left:0;top:3071px;width:1200px;height:222px;background:var(--white)}
.blog-heading{left:0;top:2868px;width:1200px;text-align:center;font-size:32px;color:var(--white)}
.blog-rule{left:561px;top:2922px;width:78px;height:2px;background:var(--white)}
.post{top:2945px;width:319px;height:286px;background:var(--white);box-shadow:0 2px 6px rgba(0,0,0,.12);border-bottom:4px solid #cfcfcf}
.post.featured{border-bottom-color:var(--green)}
.post-date{left:21px;top:26px;width:57px;height:59px;background:#b5b5b5;color:var(--white);text-align:center}
.post.featured .post-date{background:var(--green)}
.post-date b{display:block;font-size:24px;font-weight:500;line-height:32px}
.post-date span{font-size:8px;letter-spacing:.5px}
.post-title{left:21px;top:112px;width:285px;font-family:"Exo 2",sans-serif;font-weight:400;font-size:20px;line-height:28px;color:var(--ink)}
.post-text{left:21px;top:178px;width:285px;font-size:12px;line-height:24px;color:#444}
.post-more{left:21px;top:244px;font-size:11px;font-weight:600;color:#333;letter-spacing:.5px}

/* footer */
.site-footer{left:0;top:3293px;width:1200px;height:231px;background:var(--light)}
.footer-nav{left:0;top:3362px;width:1200px;display:flex;justify-content:center;gap:42px;font-size:12.5px;color:#333}
.footer-social{left:0;top:3407px;width:1200px;display:flex;justify-content:center;gap:12px}
.footer-social .social{width:34px;height:34px}
.footer-line{left:111px;top:3470px;width:987px;height:1px;background:#dcdcdc}
.copyright{left:111px;top:3486px;font-size:11px;color:#333}
.copyright em{font-style:normal;color:var(--green)}
</style>
</head>
<body>

<header class="abs site-header">
  <div class="abs brand"><span class="brand-dot"></span><span class="brand-name">Tervane</span></div>
  <div class="abs top-bar">
    <span class="contact">
      <svg width="14" height="14" viewBox="0 0 24 24" fill="#fff"><path d="M6.6 10.8a15 15 0 0 0 6.6 6.6l2.2-2.2a1 1 0 0 1 1-.25 11.4 11.4 0 0 0 3.6.57 1 1 0 0 1 1 1V20a1 1 0 0 1-1 1A17 17 0 0 1 3 4a1 1 0 0 1 1-1h3.5a1 1 0 0 1 1 1 11.4 11.4 0 0 0 .57 3.6 1 1 0 0 1-.25 1z"/></svg>
      555-218-4470
    </span>
    <span class="contact">
      <svg width="15" height="12" viewBox="0 0 24 18" fill="none" stroke="#fff" stroke-width="2"><rect x="1" y="1" width="22" height="16"/><path d="M1 1l11 9 11-9"/></svg>
      info@tervaneinspect.com
    </span>
    <span class="socials"><span class="social s1"></span><span class="social s2"></span><span class="social s3"></span><span class="social s4"></span></span>
  </div>
  <nav class="abs main-nav">
    <span class="active">HOME</span><span>OUR SERVICES</span><span>RESOURCES</span><span>BLOG</span><span>Q&amp;A</span><span>REVIEWS</span><span>CONNECT</span>
  </nav>
</header>

<section>
  <div class="abs hero" role="img" aria-label="Photo of a two-storey house with a garden of flowering shrubs and lawn"></div>
  <div class="abs hero-frame"></div>
  <div class="abs frame-top" style="left:246px;width:60px"></div>
  <div class="abs frame-top" style="left:894px;width:60px"></div>
  <h1 class="abs hero-title">Fast Dependable Results<br>When IT Matters The Most</h1>
  <a class="abs btn hero-btn">CALL NOW</a>
</section>

<section>
  <div class="abs service-panel"></div>
  <h2 class="abs service-title">SERVICE</h2>
  <p class="abs service-text">Lorem Ipsum is simply dummy text of the printing and typesetting industry. Lorem Ipsum has been the industry's standard dummy !</p>
  <div class="abs service-card card-a" role="img" aria-label="Photo of a suburban house with a garage"></div>
  <div class="abs service-card card-b" role="img" aria-label="Photo of a modern apartment building"></div>
  <div class="abs service-card card-c" role="img" aria-label="Photo of a business handshake"></div>
  <div class="abs service-label label-a">Asbestos Testing</div>
  <div class="abs service-label label-b">Mold Testing</div>
  <div class="abs service-label label-c">Lead Based Paint Testing</div>
</section>

<section>
  <div class="abs project-band"></div>
  <h2 class="abs project-title">New construction project!</h2>
  <p class="abs project-text">Let us start you in the right direction with our certified asbestos inspections . Residential, commercial, schools, governmental properties, multi-family and more.</p>
  <a class="abs btn project-btn">CALL NOW</a>
</section>

<section>
  <h2 class="abs section-heading env-heading">ENVIRONMENTAL<br>TESTING</h2>
  <div class="abs rule env-rule"></div>
  <div class="abs body-copy env-copy">
    <p>Lorem Ipsum is simply dummy text of the printing and typesetting industry. Lorem Ipsum has been the industry's standard dummy text ever since the 1500s, when an unknown printer took a galley of type and scrambled it to make a type specimen book.</p>
    <p>Lorem Ipsum is simply dummy text of the printing and typesetting industry. Lorem Ipsum has been the industry's standard dummy text ever since the 1500s, when an unknown printer took .</p>
  </div>
  <div class="abs env-media-a" role="img" aria-label="Video still of an apartment block beside a tree-lined walkway"></div>
  <div class="abs env-media-b" role="img" aria-label="Video still of a family house with a front garden"></div>
  <svg class="abs play" style="left:707px" viewBox="0 0 34 34"><path d="M13 10l11 7-11 7z" fill="#fff"/></svg>
  <svg class="abs play" style="left:956px" viewBox="0 0 34 34"><path d="M13 10l11 7-11 7z" fill="#fff"/></svg>
</section>

<section>
  <div class="abs about" role="img" aria-label="Faded photo of a city skyline"></div>
  <svg class="abs about-shape" width="1200" height="378" viewBox="0 0 1200 378">
    <polygon points="484,0 1200,0 1200,378 530,378" fill="#ffffff"/>
    <polygon points="1090,0 1200,0 1200,378 1150,378" fill="#ececec"/>
  </svg>
  <div class="abs about-pill"></div>
  <div class="abs about-photo" role="img" aria-label="Portrait photo of the company owner"></div>
  <h2 class="abs section-heading about-heading">ABOUT ME</h2>
  <div class="abs about-rule"></div>
  <div class="abs body-copy about-copy">
    <p>Lorem Ipsum is simply dummy text of the printing and typesetting industry. Lorem Ipsum has been the industry's standard dummy text ever since the 1500s, when an unknown printer took a galley of type and scrambled it to make a type specimen book.</p>
    <p>Lorem Ipsum is simply dummy text of the printing and typesetting industry. Lorem Ipsum has been the industry's standard dummy text ever since the 1500s, when an unknown printer .</p>
  </div>
  <div class="abs signature">DALE VERRIN</div>
  <div class="abs owner">Owner</div>
</section>

<section>
  <div class="abs badges"></div>
  <div class="abs badge" style="left:118px;top:2329px;width:86px;height:86px;border-radius:50%"></div>
  <div class="abs badge" style="left:250px;top:2346px;width:138px;height:52px;border-radius:6px"></div>
  <div class="abs badge" style="left:450px;top:2346px;width:224px;height:52px;border-radius:4px"></div>
  <div class="abs badge" style="left:750px;top:2344px;width:110px;height:56px;border-radius:4px"></div>
  <div class="abs badge" style="left:950px;top:2347px;width:50px;height:50px;border-radius:50%"></div>
  <div class="abs badge" style="left:1010px;top:2360px;width:80px;height:24px;border-radius:3px"></div>
</section>

<section>
  <h2 class="abs section-heading testi-heading">TESTIMONAL</h2>
  <div class="abs testi-rule"></div>
  <blockquote class="abs quote" style="left:253px">Lorem Ipsum is simply dummy text of the printing and typesetting industry. Lorem Ipsum has been the industry's standard dummy text ever since.</blockquote>
  <blockquote class="abs quote" style="left:612px">Lorem Ipsum is simply dummy text of the printing and typesetting industry. Lorem Ipsum has been the industry's standard dummy text ever since.</blockquote>
  <div class="abs avatar av1" role="img" aria-label="Customer photo"></div>
  <div class="abs avatar av2" role="img" aria-label="Customer photo"></div>
  <div class="abs person" style="left:248px">Marla</div>
  <div class="abs person" style="left:613px">Tomas</div>
  <div class="abs stars" style="left:248px">★★★★★</div>
  <div class="abs stars" style="left:613px">★★★★★</div>
</section>

<section>
  <div class="abs blog-band"></div>
  <div class="abs blog-base"></div>
  <h2 class="abs section-heading blog-heading">RECENT BLOG</h2>
  <div class="abs blog-rule"></div>

  <article class="abs post" style="left:111px">
    <div class="abs post-date"><b>6</b><span>JAN 2018</span></div>
    <h3 class="abs post-title">Lorem Ipsum is simply dummy printing typesetting industry.</h3>
    <p class="abs post-text">long established fact that a reader will be distracted by the readable content of a page</p>
    <a class="abs post-more">READ MORE »</a>
  </article>
  <article class="abs post featured" style="left:446px">
    <div class="abs post-date"><b>6</b><span>JAN 2018</span></div>
    <h3 class="abs post-title">Lorem Ipsum is simply dummy printing typesetting industry.</h3>
    <p class="abs post-text">long established fact that a reader will be distracted by the readable content of a page</p>
    <a class="abs post-more">READ MORE »</a>
  </article>
  <article class="abs post" style="left:780px">
    <div class="abs post-date"><b>6</b><span>JAN 2018</span></div>
    <h3 class="abs post-title">Lorem Ipsum is simply dummy printing typesetting industry.</h3>
    <p class="abs post-text">long established fact that a reader will be distracted by the readable content of a page</p>
    <a class="abs post-more">READ MORE »</a>
  </article>
</section>

<footer class="abs site-footer"></footer>
<nav class="abs footer-nav"><span>Home</span><span>Our Services</span><span>Resources</span><span>Blog</span><span>Q&amp;A</span><span>Reviews</span><span>Connect</span></nav>
<div class="abs footer-social"><span class="social s1"></span><span class="social s2"></span><span class="social s3"></span><span class="social s4"></span></div>
<div class="abs footer-line"></div>
<p class="abs copyright">©copyright, 2018 <em>Tervane Inspections</em> All Right Reserved</p>

</body>
</html>
```